Safety Consultancy focusing on developing exceptional Safety Leaders

I need a full but simple, modern, catchy website to drive business - my focus is on helping organizations to understand the impact that leaders have on safety performance and how they build the processes to make that happen. I already have great branding (logos) built through ArtisanHive and can provide all narrative to build out the pages

Target Market(s)

Focused internationally. Typical client has a fairly robust and mature safety culture yet lacks the focused effort to develop all levels of leadership in terms of managing safety. Exercising these competencies results in continued development of an organizations safety culture as well as improved safety performance

Industry/Entity Type

all

Coding

Coded - Design and coding required

Number of Pages Required

4 page

Font styles to use
Other font styles liked:
• to match my branding

Colors
0054AA
0677BA
7BADD7
CADEEF
E8F1F8

Requirements
Must have
• Must utilize my current branding, logo, etc. I want to have a page outlining clearly my vision - which I will add to my uploads as we move forward. I need to have a page listing my extensive and unique experience as well as successes
Nice to have
• Want to leave it up to designers - but needs to be simple and easily navigable - hope to have a resource page that I can update myself with safety resource info, reports, etc.

```html
<!DOCTYPE html>
<html lang="en">
<head>
<meta charset="utf-8">
<title>Harlow Ridge Ventures International — Safety Leadership</title>
<link rel="stylesheet" href="https://fonts.googleapis.com/css2?family=Lexend:wght@300;400;500;600&family=Poppins:wght@400;500&display=swap">
<style>
:root{
  --ink:#2d2a8c;
  --ink-dark:#23207a;
  --blue:#0054AA;
  --sky:#0677BA;
  --soft:#7BADD7;
  --mist:#CADEEF;
  --pale:#E8F1F8;
  --accent:#3f74d6;
  --text:#5a5a66;
  --field:#eceef2;
  --white:#ffffff;
}
*{margin:0;padding:0;box-sizing:border-box}
html,body{width:1200px;height:4471px;overflow:hidden}
body{position:relative;background:var(--white);font-family:"Lexend",sans-serif;color:var(--ink-dark)}
.abs{position:absolute}
.hl{color:var(--accent)}
.eyebrow{font-size:19px;font-weight:400;color:var(--ink)}
.title{font-size:38px;font-weight:400;line-height:1.14;color:#121236}
.copy{font-family:"Poppins",sans-serif;font-size:12px;line-height:1.25;color:var(--text)}
.btn{display:inline-flex;align-items:center;justify-content:center;background:var(--ink);color:var(--white);border-radius:6px;font-size:15px;font-weight:400}

/* top bar & nav */
.topbar{top:0;left:0;width:1200px;height:38px;background:var(--ink);color:var(--white);font-size:13px}
.topbar .hours{left:75px;top:11px}
.topbar .currency{right:60px;top:11px}
.nav{top:38px;left:0;width:1200px;height:68px;background:var(--white)}
.brand{display:flex;align-items:center;gap:10px}
.brand .mark{width:30px;height:30px;border-radius:50%;background:var(--ink)}
.brand .name{font-size:17px;font-weight:500;color:var(--ink);line-height:1}
.nav .brand{left:60px;top:20px}
.menu{right:60px;top:25px;display:flex;gap:33px;font-size:15px;color:#15153a}

/* hero */
.hero{top:106px;left:0;width:1200px;height:712px}
.hero-photo{position:absolute;inset:0;background:radial-gradient(circle at 50% 48%,#6fb1e8 0%,#2f7fc3 28%,#2f6f9d 55%,#3d8a6a 85%,#2f7a44 100%);clip-path:polygon(0 0,100% 0,100% 648px,50% 706px,0 648px)}
.hero-tab{position:absolute;left:0;top:0;width:1200px;height:712px}
.hero .welcome{top:108px;left:0;width:1200px;text-align:center;font-size:18px;color:var(--ink)}
.hero h1{position:absolute;top:140px;left:0;width:1200px;text-align:center;font-size:52px;font-weight:400;line-height:1.18;color:var(--white)}
.hero h1 .dk{color:var(--ink)}
.hero .lead{top:344px;left:150px;width:900px;text-align:center;font-family:"Poppins",sans-serif;font-size:11.5px;line-height:1.3;color:var(--white)}
.hero .btn{top:420px;left:528px;width:145px;height:40px;border-radius:10px}
.dots{top:616px;left:536px;display:flex;gap:10px;align-items:center}
.dots span{width:14px;height:14px;border:1.5px solid var(--white);border-radius:50%}
.dots span.on{width:22px;height:22px;background:var(--white)}
.social-rail{top:338px;right:0;width:46px;height:216px;background:var(--white);border-radius:8px 0 0 8px;display:flex;flex-direction:column;align-items:center;justify-content:space-evenly}
.social-rail span{width:14px;height:14px;border-radius:50%;background:var(--ink)}

/* about */
.about-photo-a{top:910px;left:61px;width:365px;height:262px;background:linear-gradient(135deg,#d7d4cf,#9a9088 60%,#5c5a60)}
.about-photo-b{top:1025px;left:170px;width:420px;height:325px;background:linear-gradient(160deg,#c8a58a,#8a6b58 45%,#3c3c46)}
.about-dot{top:978px;left:523px;width:70px;height:70px;border-radius:50%;background:#f0f0f3}
.about-text{top:922px;left:615px;width:535px}
.about-text .title{margin-top:12px;margin-bottom:16px;font-size:37px;white-space:nowrap}
.about-text .copy{margin-bottom:12px}
.about-meta{display:flex;align-items:center;gap:54px;margin-top:16px}
.founder{display:flex;align-items:center;gap:14px}
.avatar{width:56px;height:56px;border-radius:50%;border:3px solid var(--ink);background:linear-gradient(135deg,#9fb4cf,#4a5c7a)}
.signature{width:120px;height:34px;background:linear-gradient(90deg,#e9e9ef,#f6f6f8)}
.founder .role{font-size:12px;color:#15153a;margin-top:2px}
.team{display:flex;align-items:center;gap:8px}
.team b{font-size:26px;font-weight:400;color:var(--ink)}
.team span{font-size:15px;line-height:1.1;color:#15153a}
.about-btn{margin-top:26px;width:162px;height:40px}

/* partners */
.partners{top:1410px;left:0;width:1200px;height:50px;display:flex;justify-content:space-between;align-items:center;padding:0 10px;font-size:32px;font-weight:500;color:var(--ink)}

/* help */
.help-head{top:1510px;left:0;width:1200px;text-align:center}
.help-head .title{margin-top:12px}
.help-cols{top:1675px;left:60px;width:1080px;display:flex;justify-content:space-between}
.help-col{width:350px;text-align:center}
.help-col svg{width:64px;height:64px}
.help-col h3{font-size:15px;font-weight:400;color:#15153a;margin:12px 0 14px}
.help-col .copy{font-size:11.5px}

/* experience */
.exp{top:1959px;left:0;width:1200px;height:525px;background:linear-gradient(100deg,#1d5cc2 0%,#2f77d6 45%,#8bb6e8 70%,#eaf1fa 100%)}
.exp-photo{top:1972px;left:605px;width:595px;height:500px;background:linear-gradient(135deg,#c9d3df,#8a98ab 40%,#46506a 80%);clip-path:polygon(25% 0,100% 0,100% 100%,25% 100%,0 50%)}
.exp-text{top:2020px;left:60px;width:530px;color:var(--white)}
.exp-text .eyebrow{color:var(--white)}
.exp-text .title{color:var(--white);margin:12px 0 16px}
.exp-text .copy{color:var(--white);margin-bottom:10px}
.exp-stats{display:flex;gap:42px;color:var(--white);margin-top:14px}
.exp-stats div{display:flex;align-items:center;gap:10px}
.exp-stats b{font-size:26px;font-weight:400}
.exp-stats span{font-size:15px;line-height:1.15}
.exp-btn{margin-top:30px;width:164px;height:40px}

/* services */
.svc-head{top:2572px;left:0;width:1200px;text-align:center}
.svc-head .title{margin-top:12px}
.svc-lines{top:2740px;left:0;width:1200px;height:340px}
.svc-center{top:2850px;left:470px;width:260px;text-align:center;font-size:44px;font-weight:500;color:var(--ink);line-height:1}
.card{width:370px;height:92px;border:2px solid var(--ink);border-radius:8px;background:var(--white);padding:8px 14px}
.card h4{font-size:12.5px;font-weight:400;color:#15153a;margin-bottom:3px}
.card .copy{font-size:9.5px;line-height:1.2}
.card .more{font-size:9.5px;color:#15153a;margin-top:2px}
.card.left{padding-right:60px}
.card.right{padding-left:72px}
.card.solid{background:var(--ink);border-color:var(--ink)}
.card.solid h4,.card.solid .copy,.card.solid .more{color:var(--white)}
.node{width:58px;height:58px;border-radius:50%;background:var(--ink);border:3px solid var(--white);box-shadow:0 0 0 2px var(--ink);display:flex;align-items:center;justify-content:center}
.node.light{background:var(--white)}
.node svg{width:30px;height:30px}

/* results */
.res-head{top:3152px;left:0;width:1200px;text-align:center}
.res-head .title{margin-top:12px}
.stats{top:3322px;left:60px;width:1080px;display:flex;justify-content:space-between}
.stat{width:270px;text-align:center}
.stat b{display:block;font-size:33px;font-weight:400;color:var(--accent)}
.stat span{display:block;font-size:15px;color:#15153a;line-height:1.25;margin-top:4px}

/* contact */
.contact-text{top:3538px;left:60px;width:390px}
.contact-text .title{margin:10px 0 14px}
.info{display:flex;gap:12px;align-items:flex-start}
.info svg{width:26px;height:26px;flex:none}
.info b{display:block;font-size:15px;font-weight:400;color:#15153a}
.info span{font-size:12px;color:#15153a}
.info-mail{top:3768px;left:60px}
.info-call{top:3768px;left:335px}
.info-addr{top:3825px;left:60px}
.field{background:var(--field);border-radius:4px;font-size:13px;color:#15153a;padding:13px 20px}
.submit{top:3851px;left:519px;width:622px;height:40px;border-radius:6px}

/* footer */
.footer{top:3975px;left:0;width:1200px;height:496px}
.footer-logo{top:4080px;left:0;width:1200px;text-align:center;font-size:52px;font-weight:500;color:var(--white);line-height:1}
.footer-logo small{display:block;font-size:20px;font-weight:500;margin-top:4px}
.fcol{top:4225px;color:var(--white)}
.fcol h5{font-size:15px;font-weight:400;margin-bottom:12px}
.fcol p{font-family:"Poppins",sans-serif;font-size:10px;line-height:2.3}
.fcol .tight{line-height:1.25}
.fdots{display:flex;gap:10px;margin-top:12px}
.fdots span{width:16px;height:16px;border-radius:50%;background:var(--white)}
.fline{display:flex;align-items:center;gap:10px}
.fline svg{width:14px;height:14px}
.copyright{top:4434px;left:0;width:1200px;text-align:center;font-size:10px;color:var(--white)}
</style>
</head>
<body>

<!-- top bar -->
<div class="abs topbar">
  <span class="abs hours">Monday - Friday: 8:00 AM - 9:00 PM</span>
  <span class="abs currency">USD &#8963;</span>
</div>

<!-- navigation -->
<header class="abs nav">
  <div class="abs brand"><span class="mark"></span><span class="name">Harlow Ridge Ventures</span></div>
  <nav class="abs menu">
    <span>Home</span><span>About Us</span><span>Experience &amp; Successes</span><span>Services</span><span>Vision</span><span>Contact Us</span>
  </nav>
</header>

<!-- hero -->
<section class="abs hero">
  <svg class="hero-tab" viewBox="0 0 1200 712" aria-hidden="true"><polygon points="0,648 600,706 1200,648 1200,660 600,712 0,660" fill="#2d2a8c"/><polygon points="540,700 600,712 660,700 600,690" fill="#2d2a8c"/></svg>
  <div class="hero-photo" role="img" aria-label="Cupped hands holding a glowing globe above green grass"></div>
  <p class="abs welcome">Welcome To Harlow Ridge Ventures International</p>
  <h1>Empowering <span class="dk">Leaders To</span> Transform<br><span class="dk">Safety Cultures</span> And <span class="dk">Drive</span><br>Performance <span class="dk">Excellence</span></h1>
  <p class="abs lead">Lorem Ipsum Dolor Sit Amet Consectetur. Semper Nullam Id Est Auctor Tristique Volutpat. Mi Phasellus Pellentesque Et Montes. Lectus Pulvinar Ut Massa Suspendisse Nec In. Massa Cursus Pellentesque Pulvinar Nunc Enim Dignissim Adipiscing Ultricies. Leo Blandit In Non Ultricies Viverra Odio Vel Nunc Sed. Mi Ornare Ut Arcu Aliquam Nec Massa. Facilisis Auctor Molestie Sed Augue. Diam Facilisi Tristique.</p>
  <span class="abs btn">Get Started</span>
  <div class="abs dots"><span></span><span></span><span class="on"></span><span></span><span></span></div>
</section>
<div class="abs social-rail"><span></span><span></span><span></span><span></span><span></span></div>

<!-- about -->
<div class="abs about-photo-a" role="img" aria-label="Group of business professionals standing in an office"></div>
<div class="abs about-dot"></div>
<div class="abs about-photo-b" role="img" aria-label="Presenter leading a safety training session"></div>
<div class="abs about-text">
  <p class="eyebrow">About Us</p>
  <h2 class="title">Pioneers In <span class="hl">Safety</span> Leadership</h2>
  <p class="copy">Lorem Ipsum Dolor Sit Amet Consectetur. Semper Nullam Id Est Auctor Tristique Volutpat. Mi Phasellus Pellentesque Et Montes. Lectus Pulvinar Ut Massa Suspendisse Nec In. Massa Cursus Pellentesque Pulvinar Nunc Enim Dignissim Adipiscing Ultricies. Leo Blandit In Non Ultricies Viverra Odio Vel Nunc Sed. Mi Ornare Ut Arcu Aliquam Nec Massa. Facilisis Auctor Molestie Sed Augue. Diam Facilisi Tristique.</p>
  <p class="copy">Lorem Ipsum Dolor Sit Amet Consectetur. Semper Nullam Id Est Auctor Tristique Volutpat. Mi Phasellus Pellentesque Et Montes. Lectus Pulvinar Ut Massa Suspendisse Nec In. Massa Cursus Pellentesque Pulvinar Nunc Enim</p>
  <p class="copy">Leo Blandit In Non Ultricies Viverra Odio Vel Nunc Sed. Mi Ornare Ut Arcu Aliquam Nec Massa. Facilisis Auctor Molestie Sed Augue. Diam Facilisi Tristique.</p>
  <div class="about-meta">
    <div class="founder">
      <div class="avatar" role="img" aria-label="Portrait of the founder"></div>
      <div><div class="signature" role="img" aria-label="Founder signature"></div><p class="role">The Founder</p></div>
    </div>
    <div class="team"><b>250+</b><span>Expert Team<br>Member</span></div>
  </div>
  <span class="btn about-btn">Discover More</span>
</div>

<!-- partners -->
<div class="abs partners"><span>quillpath</span><span>Norvane</span><span>TIDEWELL FUNDS</span><span>VEXA</span><span>Meridel</span></div>

<!-- how we help -->
<div class="abs help-head">
  <p class="eyebrow">How We Help You</p>
  <h2 class="title">Your Satisfaction Our <span class="hl">Priority</span><br><span class="hl">Every Step</span> Of The Way</h2>
</div>
<div class="abs help-cols">
  <div class="help-col">
    <svg viewBox="0 0 64 64" fill="none" stroke="#2d2a8c" stroke-width="2.5"><circle cx="28" cy="26" r="15"/><path d="M20 42v14h18v-8M43 14l8-8M47 22h8"/><circle cx="28" cy="24" r="5"/></svg>
    <h3>Understand Customer Needs</h3>
    <p class="copy">We Start By Listening To Customer Feedback And Concerns To Understand Their Needs. By Identifying Common Issues, We Tailor Our Support To Address Specific Challenges, Ensuring A Personalized And Effective Experience For Every Customer.</p>
  </div>
  <div class="help-col">
    <svg viewBox="0 0 64 64" fill="none" stroke="#2d2a8c" stroke-width="2.5"><circle cx="30" cy="34" r="16"/><path d="M14 34a16 16 0 0 1 32 0M36 6h22v16H44l-6 5v-5"/><path d="M42 14h12"/></svg>
    <h3>Provide Clear And Accessible Support</h3>
    <p class="copy">We Offer Support Through Phone, Email, And Live Chat To Suit Your Needs. Our Website Features Clear FAQs And Guides For Quick Help. We Are Committed To Timely And Effective Responses. Your Satisfaction Is Our Priority.</p>
  </div>
  <div class="help-col">
    <svg viewBox="0 0 64 64" fill="none" stroke="#2d2a8c" stroke-width="2.5"><circle cx="32" cy="32" r="24"/><path d="M22 42V34M30 42V26M38 42V30M46 42V20M18 44h30"/></svg>
    <h3>Follow Up And Improve</h3>
    <p class="copy">After Resolving Issues, We Follow Up To Ensure Satisfaction And Address Any Further Needs. We Gather Feedback To Understand Your Experience And Make Necessary Improvements. Our Goal Is Continuous Enhancement Based On Your Input.</p>
  </div>
</div>

<!-- experience -->
<section class="abs exp"></section>
<div class="abs exp-photo" role="img" aria-label="Smiling colleagues working together at a laptop"></div>
<div class="abs exp-text">
  <p class="eyebrow">Experience &amp; Successes</p>
  <h2 class="title">Showcasing Our Journey<br>And Achievements</h2>
  <p class="copy">Lorem Ipsum Dolor Sit Amet Consectetur. Semper Nullam Id Est Auctor Tristique Volutpat. Mi Phasellus Pellentesque Et Montes. Lectus Pulvinar Ut Massa Suspendisse Nec In. Massa Cursus Pellentesque Pulvinar Nunc Enim Dignissim Adipiscing Ultricies. Leo Blandit In Non Ultricies Viverra Odio Vel Nunc Sed. Mi Ornare Ut Arcu Aliquam Nec Massa. Facilisis Auctor Molestie Sed Augue. Diam Facilisi Tristique.</p>
  <p class="copy">Lorem Ipsum Dolor Sit Amet Consectetur. Semper Nullam Id Est Auctor Tristique Volutpat. Mi Phasellus Pellentesque Et Montes. Lectus Pulvinar Ut Massa Suspendisse Nec In. Massa Cursus Pellentesque Pulvinar Nunc Enim</p>
  <div class="exp-stats">
    <div><b>2023</b><span>Award-Winning<br>Safety Leadership</span></div>
    <div><b>40%</b><span>Successful Project<br>Implementations</span></div>
  </div>
  <span class="btn exp-btn">Discover More</span>
</div>

<!-- services -->
<div class="abs svc-head">
  <p class="eyebrow">Our Services</p>
  <h2 class="title">Comprehensive <span class="hl">Support</span> For<br>Every <span class="hl">Challenge</span></h2>
</div>
<svg class="abs svc-lines" viewBox="0 0 1200 340" fill="none" stroke="#2d2a8c" stroke-width="1.5" aria-hidden="true">
  <path d="M458 46 C520 46 540 80 560 120"/>
  <path d="M414 159 H520"/>
  <path d="M458 271 C520 271 540 240 560 200"/>
  <path d="M742 46 C680 46 660 80 640 120"/>
  <path d="M786 159 H680"/>
  <path d="M742 280 C680 280 660 240 640 200"/>
</svg>
<div class="abs svc-center">Harlow<br>Ridge</div>

<div class="abs card left" style="top:2740px;left:104px">
  <h4>Consulting For Safety Performance</h4>
  <p class="copy">Lorem Ipsum Dolor Sit Amet Consectetur. Diam Sit Tristique Gravida Consequat. Gravida Iaculis Volutpat Mi Pulvinar In. Orci Cras Ut Neque.</p>
  <p class="more">Read More &raquo;</p>
</div>
<div class="abs node" style="top:2757px;left:401px"><svg viewBox="0 0 30 30" fill="none" stroke="#fff" stroke-width="2"><rect x="5" y="6" width="20" height="14" rx="2"/><path d="M9 16l4-4 3 3 5-5M10 24h10"/></svg></div>

<div class="abs card left" style="top:2853px;left:61px">
  <h4>Safety Leadership Training</h4>
  <p class="copy">Lorem Ipsum Dolor Sit Amet Consectetur. Diam Sit Tristique Gravida Consequat. Gravida Iaculis Volutpat Mi Pulvinar In. Orci Cras Ut Neque.</p>
  <p class="more">Read More &raquo;</p>
</div>
<div class="abs node" style="top:2870px;left:357px"><svg viewBox="0 0 30 30" fill="none" stroke="#fff" stroke-width="2"><circle cx="15" cy="9" r="4"/><circle cx="7" cy="19" r="3"/><circle cx="23" cy="19" r="3"/><path d="M9 15h12M4 27h22"/></svg></div>

<div class="abs card left" style="top:2965px;left:104px">
  <h4>Safety Culture Development</h4>
  <p class="copy">Lorem Ipsum Dolor Sit Amet Consectetur. Diam Sit Tristique Gravida Consequat. Gravida Iaculis Volutpat Mi Pulvinar In. Orci Cras Ut Neque.</p>
  <p class="more">Read More &raquo;</p>
</div>
<div class="abs node" style="top:2982px;left:401px"><svg viewBox="0 0 30 30" fill="none" stroke="#fff" stroke-width="2"><circle cx="10" cy="10" r="3"/><circle cx="20" cy="10" r="3"/><path d="M4 22c0-4 3-7 6-7s6 3 6 7M14 22c0-4 3-7 6-7s6 3 6 7"/></svg></div>

<div class="abs card right" style="top:2740px;left:730px">
  <h4>Custom Safety Solutions</h4>
  <p class="copy">Lorem Ipsum Dolor Sit Amet Consectetur. Diam Sit Tristique Gravida Consequat. Gravida Iaculis Volutpat Mi Pulvinar In. Orci Cras Ut Neque.</p>
  <p class="more">Read More &raquo;</p>
</div>
<div class="abs node" style="top:2757px;left:741px"><svg viewBox="0 0 30 30" fill="none" stroke="#fff" stroke-width="2"><path d="M15 4l9 4v6c0 6-4 10-9 12-5-2-9-6-9-12V8z"/><path d="M11 15l3 3 5-6"/></svg></div>

<div class="abs card right" style="top:2853px;left:773px">
  <h4>Workshops And Seminars</h4>
  <p class="copy">Lorem Ipsum Dolor Sit Amet Consectetur. Diam Sit Tristique Gravida Consequat. Gravida Iaculis Volutpat Mi Pulvinar In. Orci Cras Ut Neque.</p>
  <p class="more">Read More &raquo;</p>
</div>
<div class="abs node" style="top:2870px;left:784px"><svg viewBox="0 0 30 30" fill="none" stroke="#fff" stroke-width="2"><rect x="4" y="5" width="22" height="15" rx="1"/><path d="M15 20v6M9 26h12M9 15l4-4 3 3 5-5"/></svg></div>

<div class="abs card right solid" style="top:2974px;left:730px">
  <h4>Safety Assessments And Audits</h4>
  <p class="copy">Lorem Ipsum Dolor Sit Amet Consectetur. Diam Sit Tristique Gravida Consequat. Gravida Iaculis Volutpat Mi Pulvinar In. Orci Cras Ut Neque.</p>
  <p class="more">Read More &raquo;</p>
</div>
<div class="abs node light" style="top:2991px;left:741px"><svg viewBox="0 0 30 30" fill="none" stroke="#2d2a8c" stroke-width="2"><circle cx="15" cy="15" r="10"/><circle cx="15" cy="15" r="4"/><path d="M15 2v4M15 24v4M2 15h4M24 15h4"/></svg></div>

<!-- results -->
<div class="abs res-head">
  <p class="eyebrow">Achieve Real Results</p>
  <h2 class="title">Comprehensive <span class="hl">Support</span> For<br>Every <span class="hl">Challenge</span></h2>
</div>
<div class="abs stats">
  <div class="stat"><b>30%</b><span>Improvement In Safety<br>Metrics</span></div>
  <div class="stat"><b>117%</b><span>Increase In Employee<br>Engagement</span></div>
  <div class="stat"><b>113451+</b><span>Metric Tons Of Market-Based<br>Scope 2 CO2 Emissions<br>Reduced</span></div>
  <div class="stat"><b>70-80%</b><span>Increase In Disclosure<br>Compliance Efficiency</span></div>
</div>

<!-- contact -->
<div class="abs contact-text">
  <p class="eyebrow">Contact Us</p>
  <h2 class="title">Let's Talk About Your<br><span class="hl">Safety Goals</span></h2>
  <p class="copy">Lorem Ipsum Dolor Sit Amet Consectetur. Eu Nulla Vulputate Sit Amet. Sit Cum Consectetur At Sit Libero. Leo Adipiscing Sed Leo Nibh Vitae Cras Dictum Pellentesque Ipsum. Felis Hendrerit Est Tellus Amet Nunc Varius. Dapibus Nec Suspendisse Urna Quis.</p>
</div>
<div class="abs info info-mail">
  <svg viewBox="0 0 26 26" fill="none" stroke="#2d2a8c" stroke-width="1.8"><rect x="2" y="6" width="22" height="15" rx="2"/><path d="M2 8l11 7 11-7"/></svg>
  <div><b>Email Us</b><span>hello@harlowridge.example</span></div>
</div>
<div class="abs info info-call">
  <svg viewBox="0 0 26 26" fill="none" stroke="#2d2a8c" stroke-width="1.8"><path d="M6 3l4 5-2 3c1 3 4 6 7 7l3-2 5 4-2 4C12 24 2 14 2 5z"/></svg>
  <div><b>Call Us</b><span>(604) 555-0187</span></div>
</div>
<div class="abs info info-addr">
  <svg viewBox="0 0 26 26" fill="none" stroke="#2d2a8c" stroke-width="1.8"><path d="M13 24s-8-8-8-14a8 8 0 0 1 16 0c0 6-8 14-8 14z"/><circle cx="13" cy="10" r="3"/></svg>
  <div><b>Address</b><span>412 Alder Lane, Powell River, British Columbia, Canada V8A 2K9</span></div>
</div>
<div class="abs field" style="top:3510px;left:519px;width:300px;height:43px">Name</div>
<div class="abs field" style="top:3510px;left:841px;width:300px;height:43px">Phone Number</div>
<div class="abs field" style="top:3578px;left:519px;width:300px;height:43px">Email</div>
<div class="abs field" style="top:3578px;left:841px;width:300px;height:43px">Your Organization</div>
<div class="abs field" style="top:3646px;left:519px;width:622px;height:175px">Message</div>
<span class="abs btn submit">Submit</span>

<!-- footer -->
<svg class="abs footer" viewBox="0 0 1200 496" preserveAspectRatio="none" aria-hidden="true">
  <defs><linearGradient id="fg" x1="0" y1="0" x2="0" y2="1"><stop offset="0" stop-color="#1f63c8"/><stop offset="1" stop-color="#0054AA"/></linearGradient></defs>
  <path d="M0 72 Q300 60 520 12 Q600 -4 680 12 Q900 60 1200 72 V496 H0 Z" fill="url(#fg)"/>
  <path d="M420 40 L600 4 L780 40" fill="none" stroke="#2d2a8c" stroke-width="8"/>
</svg>
<div class="abs footer-logo">Harlow Ridge<small>Ventures International</small></div>

<div class="abs fcol" style="left:61px;width:190px">
  <h5>About Us</h5>
  <p class="tight">Lorem Ipsum Dolor Sit Amet Consectetur. Commodo Pulvinar Molesti.</p>
  <div class="fdots"><span></span><span></span><span></span><span></span></div>
</div>
<div class="abs fcol" style="left:325px">
  <h5>Services</h5>
  <p>Safety Leadership Training<br>Custom Safety Solutions<br>Safety Culture Development<br>Workshops And Seminars</p>
</div>
<div class="abs fcol" style="left:549px">
  <h5>Page</h5>
  <p>Experience &amp; Successes<br>Vision<br>About Us</p>
</div>
<div class="abs fcol" style="left:752px">
  <h5>Links</h5>
  <p>Cookies Settings<br>Privacy Policy<br>Terms Of Services</p>
</div>
<div class="abs fcol" style="left:926px">
  <h5>Contact Us</h5>
  <p class="fline"><svg viewBox="0 0 14 14" fill="none" stroke="#fff" stroke-width="1.3"><path d="M3 1l2 3-1 2c1 2 2 3 4 4l2-1 3 2-1 2C6 13 1 8 1 2z"/></svg>+1 604 555 0142</p>
  <p class="fline"><svg viewBox="0 0 14 14" fill="none" stroke="#fff" stroke-width="1.3"><path d="M7 13S2 8 2 5a5 5 0 0 1 10 0c0 3-5 8-5 8z"/><circle cx="7" cy="5" r="1.6"/></svg>118 Harbour Way, Vancouver, BC V6B 1A1</p>
  <p class="fline"><svg viewBox="0 0 14 14" fill="none" stroke="#fff" stroke-width="1.3"><rect x="1" y="3" width="12" height="9" rx="1"/><path d="M1 4l6 4 6-4"/></svg>info@harlowridge.example</p>
</div>
<p class="abs copyright">Copyright ©2024 Harlow Ridge All Right Reserved</p>

</body>
</html>
```